Rocket business card

Modern business card design, use of color is good with clean space too.

Things to include on card:

Quote: I add fuel to your optometry practice

- Eyewear Sales
- Admin Duties
- Revenue Collection
- Leadership
- Tech Adoption
- COGS Reduction
- Product Sourcing
-Medical Growth

Dalton Vessey, CEO
Glint Harbor
Text Me! 847-302-1964
dalton@glintharbor.example

```html
<!DOCTYPE html>
<html lang="en">
<head>
<meta charset="utf-8">
<title>Glint Harbor – Business Card</title>
<link rel="stylesheet" href="https://fonts.googleapis.com/css2?family=Open+Sans:wght@400;600;700;800&display=swap">
<style>
  :root {
    --orange: #ff6a00;
    --ink: #111111;
    --paper: #ffffff;
    --stage: #e9e9eb;
    --white-text: #ffffff;
  }
  * { box-sizing: border-box; margin: 0; padding: 0; }
  html, body { width: 1200px; height: 800px; overflow: hidden; }
  body {
    background: var(--stage);
    font-family: "Open Sans", Arial, sans-serif;
    position: relative;
  }
  .card {
    position: absolute;
    top: 250px;
    width: 525px;
    height: 300px;
    background: var(--paper);
    overflow: hidden;
    box-shadow: 0 6px 18px rgba(0,0,0,0.18);
  }
  .card--services { left: 50px; }
  .card--contact { left: 625px; }
  .card__shapes { position: absolute; inset: 0; width: 100%; height: 100%; }

  /* Services face */
  .tagline-band {
    position: absolute;
    left: 0; top: 16px;
    width: 320px; height: 32px;
    background: var(--ink);
    color: var(--white-text);
    font-weight: 700;
    font-size: 15px;
    line-height: 32px;
    padding-left: 20px;
    white-space: nowrap;
  }
  .service-list {
    position: absolute;
    left: 28px; top: 58px;
    list-style: none;
    color: var(--white-text);
    font-size: 15px;
    font-weight: 600;
    line-height: 19.5px;
  }
  .service-list li::before {
    content: "";
    display: inline-block;
    width: 6px; height: 6px;
    border-radius: 50%;
    background: var(--white-text);
    margin-right: 12px;
    vertical-align: middle;
  }
  .brand {
    position: absolute;
    display: flex;
    align-items: center;
    gap: 12px;
    color: var(--ink);
    font-weight: 700;
    white-space: nowrap;
  }
  .brand__dot {
    width: 36px; height: 36px;
    border-radius: 50%;
    background: var(--orange);
    flex: none;
  }
  .card--services .brand { right: 30px; top: 200px; font-size: 32px; }
  .card--contact .brand { left: 60px; top: 40px; font-size: 34px; }
  .card--contact .brand__dot { background: var(--ink); }
  .contact-tagline {
    position: absolute;
    left: 60px; top: 96px;
    color: var(--ink);
    font-weight: 600;
    font-size: 15px;
    white-space: nowrap;
  }

  /* Contact block, in the white area */
  .contact {
    position: absolute;
    right: 26px; top: 184px;
    text-align: right;
    color: var(--ink);
  }
  .contact__name { font-size: 26px; font-weight: 800; line-height: 1.1; }
  .contact__role { font-size: 15px; font-weight: 600; line-height: 1.3; }
  .contact__line {
    display: flex;
    justify-content: flex-end;
    align-items: center;
    gap: 8px;
    font-size: 15px;
    line-height: 22px;
    white-space: nowrap;
  }
  .contact__icon { width: 14px; height: 14px; flex: none; }
</style>
</head>
<body>

  <section class="card card--services" aria-label="Services side">
    <svg class="card__shapes" viewBox="0 0 525 300" aria-hidden="true">
      <path d="M0 0 H330 C318 120 250 205 130 222 C70 230 30 238 0 246 Z" fill="var(--orange)"/>
      <path d="M330 0 C318 120 250 205 130 222 C70 230 30 238 0 246" fill="none" stroke="var(--ink)" stroke-width="4"/>
      <polygon points="355,282 425,282 435,300 365,300" fill="var(--orange)"/>
      <polygon points="410,282 525,282 525,300 420,300" fill="var(--ink)"/>
    </svg>
    <div class="tagline-band">I add fuel to your optometry practice</div>
    <ul class="service-list">
      <li>Eyewear Sales</li>
      <li>Admin Duties</li>
      <li>Revenue Collection</li>
      <li>Leadership</li>
      <li>Tech Adoption</li>
      <li>COGS Reduction</li>
      <li>Product Sourcing</li>
      <li>Medical Growth</li>
    </ul>
    <div class="brand"><span class="brand__dot"></span>Glint Harbor</div>
  </section>

  <section class="card card--contact" aria-label="Contact side">
    <svg class="card__shapes" viewBox="0 0 525 300" aria-hidden="true">
      <path d="M0 0 H460 C440 110 360 168 220 176 C120 182 50 192 0 210 Z" fill="var(--orange)"/>
      <path d="M460 0 C440 110 360 168 220 176 C120 182 50 192 0 210" fill="none" stroke="var(--ink)" stroke-width="4"/>
      <polygon points="355,282 425,282 435,300 365,300" fill="var(--orange)"/>
      <polygon points="410,282 525,282 525,300 420,300" fill="var(--ink)"/>
    </svg>
    <div class="brand"><span class="brand__dot"></span>Glint Harbor</div>
    <div class="contact-tagline">I add fuel to your optometry practice</div>
    <div class="contact">
      <div class="contact__name">Dalton Vessey</div>
      <div class="contact__role">(CEO)</div>
      <div class="contact__line">847-302-1964
        <svg class="contact__icon" viewBox="0 0 14 14" aria-label="Phone"><rect width="14" height="14" fill="var(--ink)"/><path d="M4 3 L6 3 L6.5 5.5 L5.5 6.3 C6 7.5 6.7 8.2 7.8 8.6 L8.6 7.6 L11 8.1 L11 10 C7 10.5 3.5 7 4 3 Z" fill="#fff"/></svg>
      </div>
      <div class="contact__line">dalton@glintharbor.example
        <svg class="contact__icon" viewBox="0 0 14 14" aria-label="Email"><rect width="14" height="14" fill="var(--ink)"/><rect x="2.5" y="4" width="9" height="6.5" fill="none" stroke="#fff" stroke-width="1"/><path d="M2.5 4 L7 8 L11.5 4" fill="none" stroke="#fff" stroke-width="1"/></svg>
      </div>
    </div>
  </section>

</body>
</html>
```